依頼概要
■ 依頼の目的/概要
店舗名変更の為、既存の看板のデザイン一新(変更)
店舗名 ホテル ラベンダル (HOTEL LAVENDAL)

■ 重視する点/検討基準
兎に角目を引く(目立つ)、いやらしくない(直接的でない)、センスがいい!
当方人口3万人強の小さな町です。

■ 利用用途
道路沿いの看板

■ その他/注意点
看板は3種類ありサイズが
①横1200×縦2400・・・片側2車線のバイパス沿い
②横3000×縦2000・・・片側1車線、横にガソリンスタンドがある。
③横1500×縦1500・・・片側1車線の細い県道。

照明は看板の下部からアームを伸ばしてCDMランプで照らすようにします。
3つの看板は統一性をもたせて頂きたい。

```html
<!DOCTYPE html>
<html lang="ja">
<head>
<meta charset="utf-8">
<title>HOTEL LAVENDAL 看板デザイン</title>
<link rel="stylesheet" href="https://fonts.googleapis.com/css2?family=M+PLUS+Rounded+1c:wght@700;800;900&display=swap">
<style>
  :root{
    --paper:#ffffff;
    --pink:#e6a6cf;
    --lime:#c3d83a;
    --magenta:#e4007f;
    --green:#1fa046;
    --blue:#1c63c6;
    --ink:#1a1a1a;
    --red:#e60012;
    --frame:#8a8a8a;
  }
  *{margin:0;padding:0;box-sizing:border-box}
  html,body{width:766px;height:1200px;overflow:hidden;background:var(--paper)}
  body{position:relative;font-family:"M PLUS Rounded 1c",sans-serif}
  .sign{position:absolute;background:var(--paper);border:1px solid var(--frame);overflow:hidden}
  .sign-tall{left:51px;top:20px;width:276px;height:572px}
  .sign-square{left:421px;top:20px;width:335px;height:312px}
  .sign-wide{left:64px;top:745px;width:694px;height:442px}
  .backdrop{position:absolute;inset:0;width:100%;height:100%}
  .el{position:absolute;white-space:nowrap;line-height:1}
  .tagline{background:var(--blue);color:var(--paper);border-radius:999px;text-align:center;font-weight:800;display:flex;flex-direction:column;justify-content:center;align-items:center;line-height:1.2}
  .word-hotel{color:var(--magenta);font-weight:900;-webkit-text-stroke:3px var(--paper);paint-order:stroke fill;text-shadow:0 0 1px #b0006a}
  .word-name{color:var(--green);font-weight:900;-webkit-text-stroke:3px var(--paper);paint-order:stroke fill;text-shadow:0 0 1px #0d5a25}
  .phone{color:var(--ink);font-weight:900;letter-spacing:-0.5px}
  .direction{position:absolute}
  .direction svg{position:absolute;inset:0;width:100%;height:100%}
  .direction .label{position:absolute;color:var(--red);font-weight:900;white-space:nowrap;line-height:1}
</style>
</head>
<body>

<!-- Tall sign -->
<section class="sign sign-tall" aria-label="縦型看板">
  <svg class="backdrop" viewBox="0 0 276 572" preserveAspectRatio="none" aria-hidden="true">
    <polygon points="0,0 276,0 276,70 0,330" fill="var(--pink)"/>
    <polygon points="276,250 276,572 0,572 0,500" fill="var(--lime)"/>
  </svg>
  <div class="el tagline" style="left:40px;top:22px;width:206px;height:54px;font-size:17px">
    <span>ブティックホテル</span><span>ラベンダル</span>
  </div>
  <div class="el word-hotel" style="left:18px;top:96px;font-size:58px">HOTEL</div>
  <div class="el word-name" style="left:10px;top:160px;font-size:48px">LAVENDAL</div>
  <div class="el phone" style="left:14px;top:232px;font-size:27px">☎0120-000-000</div>
  <div class="direction" style="left:12px;top:392px;width:254px;height:110px">
    <svg viewBox="0 0 250 110" preserveAspectRatio="none" aria-hidden="true">
      <polygon points="7,28 150,28 150,6 243,55 150,104 150,82 7,82" fill="var(--paper)" stroke="var(--blue)" stroke-width="10" stroke-linejoin="round"/>
    </svg>
    <span class="label" style="left:22px;top:45px;font-size:21px">直進 100m</span>
  </div>
</section>

<!-- Square sign -->
<section class="sign sign-square" aria-label="小型看板">
  <svg class="backdrop" viewBox="0 0 335 312" preserveAspectRatio="none" aria-hidden="true">
    <polygon points="0,0 150,0 0,150" fill="var(--pink)"/>
    <polygon points="0,230 120,312 0,312" fill="var(--lime)"/>
    <polygon points="335,150 335,312 250,312" fill="var(--lime)"/>
  </svg>
  <div class="el word-hotel" style="left:74px;top:10px;font-size:46px">HOTEL</div>
  <div class="el word-name" style="left:12px;top:64px;font-size:55px">LAVENDAL</div>
  <div class="el phone" style="left:40px;top:140px;font-size:26px">☎0120-000-000</div>
  <div class="el tagline" style="left:12px;top:198px;width:170px;height:50px;font-size:15px">
    <span>ブティックホテル</span><span>ラベンダル</span>
  </div>
  <div class="direction" style="left:200px;top:186px;width:128px;height:82px">
    <svg viewBox="0 0 128 82" preserveAspectRatio="none" aria-hidden="true">
      <polygon points="6,22 72,22 72,5 122,41 72,77 72,60 6,60" fill="var(--paper)" stroke="var(--blue)" stroke-width="8" stroke-linejoin="round"/>
    </svg>
  </div>
</section>

<!-- Wide sign -->
<section class="sign sign-wide" aria-label="横型看板">
  <svg class="backdrop" viewBox="0 0 694 442" preserveAspectRatio="none" aria-hidden="true">
    <polygon points="0,0 460,0 0,430" fill="var(--pink)"/>
    <polygon points="694,60 694,442 300,442" fill="var(--lime)"/>
  </svg>
  <div class="el word-hotel" style="left:36px;top:44px;font-size:80px">HOTEL</div>
  <div class="el tagline" style="left:414px;top:44px;width:250px;height:70px;font-size:22px">
    <span>ブティックホテル</span><span>ラベンダル</span>
  </div>
  <div class="el word-name" style="left:30px;top:148px;font-size:104px">LAVENDAL</div>
  <div class="el phone" style="left:30px;top:340px;font-size:42px">☎0120-000-000</div>
  <div class="direction" style="left:430px;top:282px;width:254px;height:140px">
    <svg viewBox="0 0 254 140" preserveAspectRatio="none" aria-hidden="true">
      <polygon points="8,36 156,36 156,8 246,70 156,132 156,104 8,104" fill="var(--paper)" stroke="var(--blue)" stroke-width="12" stroke-linejoin="round"/>
    </svg>
    <span class="label" style="left:30px;top:58px;font-size:26px">直進 100m</span>
  </div>
</section>

</body>
</html>
```